Food Service Market Place needs 3 Banner Ads for website

We need up to 3 banner ads for a new company based in Noosa called PlatoVyn. We have created a Food Service Marketplace that connects the Food Service Suppliers such as growers, frozen food distributers, etc and restaurants, cafes, etc in real time. Our tag line is Connect|Save|Inspire and we would like three banners that would represent each item in the tag with a call to action to Register Now. These banners need to be designed to encourage chefs and small business owners to sign up.
Updates

Hi All, We have extended this for another 24 hours. Thanks.

Target Market(s)

Chefs, cafes, restaurants

Industry/Entity Type

Food Service

Contact Information for Business Card

Gareth Pellowe
Managing Director
garethp@platovyn.com.au
1300718342
0412583904
www.platovyn.com.au

Font styles to use
Sans Serif

Colors

Designer to choose colors to be used in the design.

```html
<!DOCTYPE html>
<html lang="en">
<head>
<meta charset="utf-8">
<title>PlatoVyn – Welcome Banner</title>
<link rel="stylesheet" href="https://fonts.googleapis.com/css2?family=Montserrat:wght@400;500;700&display=swap">
<style>
  :root {
    --stage: #ece7e1;
    --panel: #ffffff;
    --ink: #434a4c;
    --ink-soft: #555b5d;
    --muted: #a9adae;
    --teal: #5aa6a6;
    --teal-light: #93d6d3;
    --photo-warm: #b8664a;
    --photo-wine: #7a2a34;
    --photo-cream: #e9ddc8;
    --photo-green: #6f8d3e;
  }
  * { box-sizing: border-box; margin: 0; padding: 0; }
  html, body {
    width: 1200px; height: 1200px; overflow: hidden;
    background: var(--stage);
    font-family: "Montserrat", sans-serif;
  }
  .canvas { position: relative; width: 1200px; height: 1200px; }

  .banner-photo {
    position: absolute; left: 76px; top: 72px; width: 524px; height: 1053px;
    background:
      radial-gradient(circle at 50% 45%, var(--photo-wine) 0, rgba(122,42,52,0) 28%),
      radial-gradient(circle at 75% 80%, var(--photo-green) 0, rgba(111,141,62,0) 25%),
      radial-gradient(circle at 25% 20%, var(--photo-warm) 0, rgba(184,102,74,0) 30%),
      linear-gradient(160deg, var(--photo-cream), #c9a488 55%, #8f5a45);
  }

  .banner-panel {
    position: absolute; left: 600px; top: 114px; width: 524px; height: 966px;
    filter: drop-shadow(0 4px 10px rgba(0,0,0,0.12));
  }
  .panel-shape { position: absolute; left: 0; top: 0; }
  .panel-content { position: absolute; inset: 0; text-align: center; }
  .panel-content > * { position: absolute; }

  .brand {
    top: 100px; left: 0; right: 0;
    display: flex; align-items: center; justify-content: center; gap: 14px;
  }
  .brand-name { font-size: 62px; font-weight: 500; color: var(--ink); letter-spacing: 1px; line-height: 1; }
  .brand-dot { width: 22px; height: 22px; border-radius: 50%; background: var(--teal); }

  .divider { top: 288px; left: 163px; width: 198px; height: 10px; }

  .welcome-title {
    top: 358px; left: 0; right: 0;
    font-size: 55px; font-weight: 700; color: var(--ink); line-height: 56px;
  }
  .welcome-text {
    top: 422px; left: 0; right: 0;
    font-size: 33px; font-weight: 400; color: var(--ink-soft); line-height: 56px;
  }

  .cta {
    top: 625px; left: 79px; width: 366px; height: 82px; border-radius: 41px;
    background: linear-gradient(90deg, var(--teal), var(--teal-light));
    box-shadow: 0 10px 22px rgba(90,166,166,0.25);
    color: #fff; font-size: 27px; font-weight: 500;
    display: flex; align-items: center; justify-content: center;
  }

  .site-link { top: 902px; left: 0; right: 0; font-size: 22px; line-height: 26px; color: var(--muted); }
</style>
</head>
<body>
<main class="canvas">
  <div class="banner-photo" role="img" aria-label="Overhead photo of friends toasting with glasses of wine over a table of grilled skewers, corn, salad and bread"></div>

  <section class="banner-panel">
    <svg class="panel-shape" width="524" height="966" viewBox="0 0 524 966" aria-hidden="true">
      <path fill="#ffffff" d="M0 0 H524 V952 H522
        l-9 14 l-9 -14 l-9 14 l-9 -14 l-9 14 l-9 -14 l-9 14 l-9 -14 l-9 14 l-9 -14
        l-9 14 l-9 -14 l-9 14 l-9 -14 l-9 14 l-9 -14 l-9 14 l-9 -14 l-9 14 l-9 -14
        l-9 14 l-9 -14 l-9 14 l-9 -14 l-9 14 l-9 -14 l-9 14 l-9 -14 l-9 14 l-9 -14
        l-9 14 l-9 -14 l-9 14 l-9 -14 l-9 14 l-9 -14 l-9 14 l-9 -14 l-9 14 l-9 -14
        l-9 14 l-9 -14 l-9 14 l-9 -14 l-9 14 l-9 -14 l-9 14 l-9 -14 l-9 14 l-9 -14
        l-9 14 l-9 -14 l-9 14 l-9 -14 l-9 14 l-9 -14 l-9 14 l-9 -14 Z"/>
    </svg>

    <div class="panel-content">
      <div class="brand">
        <span class="brand-name">PlatoVyn</span>
        <span class="brand-dot"></span>
      </div>

      <svg class="divider" viewBox="0 0 198 10" aria-hidden="true">
        <line x1="0" y1="2" x2="198" y2="2" stroke="#5aa6a6" stroke-width="1.2"/>
        <line x1="36" y1="5" x2="162" y2="5" stroke="#5aa6a6" stroke-width="1.2"/>
        <line x1="36" y1="8" x2="162" y2="8" stroke="#5aa6a6" stroke-width="1.2"/>
      </svg>

      <h1 class="welcome-title">Welcome</h1>
      <p class="welcome-text">to all of you in our food<br>market place</p>

      <div class="cta">Register Now</div>

      <p class="site-link">visit site : www.platovyn.com.au</p>
    </div>
  </section>
</main>
</body>
</html>
```